Lawn maintenance
Greenmoor has you covered!
weekly , biweekly

Target Market(s)

lawn care

Industry/Entity Type

Lawn Care

Contact Information for Business Card

eye catching - not you normal "lawn business" card

Logo Text

Greenmoor Lawncare

Font styles to use
Serif
Sans Serif

Colors
ec1f27
00a990
9bcb3c
0455a3

Requirements
Must have
• Tom Halvik
• 410-555-0187
• Lawn maintenance
• Greenmoor has you covered!
• Call for a quote today!
• weekly or biweekly
Nice to have
• maybe some poker chips or playing cards
Should not have
• snow removal

```html
<!DOCTYPE html>
<html lang="en">
<head>
<meta charset="utf-8">
<title>Greenmoor Lawncare – Business Card</title>
<link rel="stylesheet" href="https://fonts.googleapis.com/css2?family=Cinzel:wght@600&family=Roboto:wght@400;500&display=swap">
<style>
  :root {
    --backdrop: #2b2b2b;
    --card-white: #f4f4f4;
    --leaf-green: #5aa61c;
    --deep-green: #1f6b04;
    --ink: #1b1b1b;
    --text-light: #ffffff;
  }
  * { margin: 0; padding: 0; box-sizing: border-box; }
  html, body {
    width: 1200px;
    height: 960px;
    overflow: hidden;
    background: var(--backdrop);
  }
  .business-card {
    position: absolute;
    left: 100px;
    top: 188px;
    width: 1000px;
    height: 583px;
    background: var(--card-white);
    overflow: hidden;
    font-family: "Roboto", Arial, sans-serif;
    color: var(--text-light);
  }
  .card-waves {
    position: absolute;
    inset: 0;
    width: 100%;
    height: 100%;
  }
  .brand {
    position: absolute;
    left: 525px;
    top: 108px;
    display: flex;
    align-items: center;
    gap: 22px;
  }
  .brand-dot {
    width: 56px;
    height: 56px;
    border-radius: 50%;
    background: var(--leaf-green);
  }
  .brand-name {
    font-family: "Cinzel", Georgia, serif;
    font-weight: 600;
    color: var(--ink);
    font-size: 50px;
    line-height: 1.0;
  }
  .brand-name span { display: block; }
  .services {
    position: absolute;
    left: 92px;
    top: 428px;
  }
  .services-title {
    font-weight: 500;
    font-size: 23px;
    letter-spacing: 0.2px;
    margin-bottom: 6px;
  }
  .services-list {
    list-style: none;
    font-size: 21px;
    line-height: 27px;
  }
  .services-list li::before {
    content: "";
    display: inline-block;
    width: 8px;
    height: 8px;
    border-radius: 50%;
    background: var(--text-light);
    margin: 0 14px 3px 0;
    vertical-align: middle;
  }
  .contact {
    position: absolute;
    right: 57px;
    top: 465px;
    text-align: right;
  }
  .contact-name {
    font-weight: 500;
    font-size: 40px;
    line-height: 1.1;
  }
  .contact-phone {
    font-weight: 500;
    font-size: 29px;
    line-height: 1.3;
  }
</style>
</head>
<body>
  <div class="business-card">
    <svg class="card-waves" viewBox="0 0 600 350" preserveAspectRatio="none" aria-hidden="true">
      <path fill="var(--leaf-green)" d="M0 272 C 80 178, 180 148, 300 172 S 480 238, 600 193 L600 350 L0 350 Z"/>
      <path fill="var(--deep-green)" stroke="#ffffff" stroke-width="1.6"
            d="M0 283 C 85 196, 185 170, 300 190 S 480 253, 600 201 L600 352 L0 352 Z"/>
    </svg>

    <div class="brand">
      <div class="brand-dot"></div>
      <div class="brand-name"><span>Greenmoor</span><span>Lawncare</span></div>
    </div>

    <div class="services">
      <h2 class="services-title">LAWN MAINTENANCE</h2>
      <ul class="services-list">
        <li>Greenmoor has you covered!</li>
        <li>Call for a quote today!</li>
        <li>weekly or biweekly</li>
      </ul>
    </div>

    <div class="contact">
      <p class="contact-name">TOM HALVIK</p>
      <p class="contact-phone">410-555-0187</p>
    </div>
  </div>
</body>
</html>
```